Enhance the web site presence of Kolrith Global Limited

Upgrade the current web site www.kolrithpanel.com to share with the audience our current plan and future developments of our company. I have created a worksheet which shows all the pages that I like to have. The home page in English, Japanese and Chinese is hyperlinked to the various pages. Under the product, we should allow the user to select "single sided PCB or double sided PCB". The translation of the contents of the pages with Japanese is not complete but the English and Chinese are complete. You can download the briefing and photos in the dropbox files below;

https://www.sharelocker.net/sh/xk4trw92mpd3ab1/BBQm_Lp841zzPq2Rw7KtYnHjEa?dl=0

Target Market(s)

Electronic companies

Industry/Entity Type

Electronic

Coding

Coded - Design and coding required

Number of Pages Required

5+ page

Font styles to use
Sans Serif

Colors
00a990
0353a1
33b8a4

Requirements
Must have
• Get a sense of confidence on our company's integrity and capability to deliver the highest quality PCBs with the most competitive prices and best services. A sense of elegance is essential as we DON'T treat profits as the number one goal. Our number goal is to do the RIGHT things right. Having a mixture of our company photos will be appropriate.

```html
<!DOCTYPE html>
<html lang="en">
<head>
<meta charset="utf-8">
<title>Kolrith Global Limited – Printed Circuit Boards</title>
<link href="https://fonts.googleapis.com/css2?family=Catamaran:wght@400;500;600;700&display=swap" rel="stylesheet">
<style>
:root{
  --green:#00a990;
  --blue:#0353a1;
  --teal:#33b8a4;
  --ink:#111;
  --body:#5a6470;
  --field:#f1f2f3;
  --soft:#f6f6f6;
  --white:#fff;
}
*{box-sizing:border-box;margin:0;padding:0}
html,body{width:1200px;height:2582px;overflow:hidden}
body{position:relative;font-family:"Catamaran",sans-serif;color:var(--ink);background:var(--white)}
.abs{position:absolute}
/* header */
.brand{left:90px;top:22px;font-size:30px;font-weight:700;color:var(--green);line-height:1;display:flex;align-items:center;gap:10px}
.brand .mark{width:14px;height:14px;background:var(--green)}
.top-contact{top:24px;font-size:14px;font-weight:500;display:flex;align-items:center;gap:7px}
.top-contact svg{fill:var(--green)}
.login{left:983px;top:18px;width:128px;height:36px;border:2px solid var(--green);border-radius:3px;color:var(--green);font-size:14px;font-weight:500;display:flex;align-items:center;justify-content:center}
.nav{left:0;top:72px;width:1200px;height:52px;background:var(--blue)}
.nav a{position:absolute;top:17px;color:#fff;font-size:14px;font-weight:500;text-decoration:none}
.nav .active-tick{position:absolute;left:308px;top:0;width:26px;height:4px;background:var(--teal)}
/* hero */
.hero{left:0;top:124px;width:1200px;height:642px;background:linear-gradient(120deg,#7b7e80 0%,#a9aaa6 40%,#c8c6bf 70%,#b48a5c 100%)}
.hero-shade{left:0;top:124px;width:1200px;height:642px;background:linear-gradient(90deg,rgba(30,30,30,.55),rgba(30,30,30,.15))}
.hero-title{left:88px;top:318px;width:720px;font-size:38px;line-height:50px;font-weight:600;color:#fff}
.hero-sub{left:90px;top:432px;font-size:17px;font-weight:500;color:#fff}
.dots{left:1150px;top:408px;display:flex;flex-direction:column;gap:9px}
.dots span{width:9px;height:9px;border:1.5px solid #fff;border-radius:50%}
.dots span.on{background:#fff}
.scroll-down{left:573px;top:636px;width:54px;height:54px;border-radius:50%;background:#fff;box-shadow:0 3px 10px rgba(0,0,0,.15);display:flex;align-items:center;justify-content:center}
/* welcome */
.welcome-title{left:90px;top:792px;font-size:32px;font-weight:600}
.welcome-rule{left:45px;top:846px;width:89px;height:3px;background:var(--green)}
.copy{font-size:13.5px;line-height:30px;color:var(--body)}
.copy p+p{margin-top:14px}
.btn-products{left:1030px;top:1028px;width:170px;height:52px;background:var(--green);color:#fff;font-size:15px;font-weight:500;display:flex;align-items:center;justify-content:center;gap:14px}
/* contact */
.contact-card{left:90px;top:1166px;width:1021px;height:475px;border:1px solid #dcdcdc;border-radius:6px;box-shadow:0 2px 8px rgba(0,0,0,.06)}
.contact-card h2{position:absolute;left:52px;top:42px;font-size:31px;font-weight:600}
.label{font-size:12px;font-weight:700}
.field{background:var(--field);font-size:12px;color:#888;padding:0 16px;display:flex;align-items:center}
.submit{left:966px;top:1563px;width:91px;height:34px;border:2px solid var(--green);border-radius:3px;color:var(--green);font-size:13px;display:flex;align-items:center;justify-content:center}
/* customers */
.customers{left:0;top:1729px;width:1200px;height:243px;background:var(--soft)}
.customers h2{position:absolute;left:0;width:1200px;top:68px;text-align:center;font-size:31px;font-weight:600}
.client{top:1868px;font-size:22px;font-weight:700;color:#555;display:flex;align-items:center;gap:8px;white-space:nowrap}
.client i{width:12px;height:12px;border-radius:50%;background:#999;display:block}
/* cta */
.cta{left:0;top:1972px;width:1200px;height:172px;background:var(--teal)}
.cta h2{position:absolute;left:90px;top:66px;font-size:32px;font-weight:600;color:#fff}
.cta-btn{left:1009px;top:2042px;width:102px;height:35px;background:#fff;border-radius:2px;font-size:13px;display:flex;align-items:center;justify-content:center}
/* footer */
.footer{left:0;top:2144px;width:1200px;height:438px;background:var(--blue)}
.foot-brand{left:90px;top:2224px;font-size:32px;font-weight:700;color:#fff}
.foot-h{top:2216px;font-size:19px;font-weight:600;color:#fff}
.foot-list{top:2256px;color:#fff;font-size:13.5px;line-height:31px;list-style:none}
.foot-list svg{fill:#fff;vertical-align:-1px;margin-right:5px}
.foot-rule{left:90px;top:2522px;width:1021px;height:1px;background:rgba(255,255,255,.2)}
.copyright{left:0;width:1200px;top:2541px;text-align:center;color:#fff;font-size:13px}
.to-top{left:1138px;top:2500px;width:42px;height:42px;border-radius:50%;background:#fff;display:flex;align-items:center;justify-content:center}
</style>
</head>
<body>

<header>
  <div class="abs brand"><span class="mark"></span>Kolrith</div>
  <div class="abs top-contact" style="left:473px">
    <svg width="13" height="13" viewBox="0 0 24 24"><path d="M6.6 10.8a15.1 15.1 0 0 0 6.6 6.6l2.2-2.2c.3-.3.7-.4 1-.2 1.1.4 2.3.6 3.6.6.6 0 1 .4 1 1V20c0 .6-.4 1-1 1A17 17 0 0 1 3 4c0-.6.4-1 1-1h3.5c.6 0 1 .4 1 1 0 1.3.2 2.5.6 3.6.1.3 0 .7-.2 1z"/></svg>
    Phone: (852) 2940 6158</div>
  <div class="abs top-contact" style="left:660px">
    <svg width="13" height="11" viewBox="0 0 24 20"><path d="M0 2h24v2L12 11 0 4zM0 6l12 7 12-7v14H0z"/></svg>
    Email: sales@kolrithpanel.com</div>
  <div class="abs top-contact" style="left:871px">
    <svg width="20" height="20" viewBox="0 0 24 24" fill="none" stroke="#222" stroke-width="1.6" style="fill:none"><circle cx="12" cy="12" r="10"/><ellipse cx="12" cy="12" rx="4.5" ry="10"/><path d="M2 12h20M4 7h16M4 17h16"/></svg>
    English <svg width="8" height="6" viewBox="0 0 8 6" style="fill:#222"><path d="M0 0h8L4 5z"/></svg></div>
  <div class="abs login">Customer Login</div>
</header>

<nav class="abs nav">
  <span class="active-tick"></span>
  <a style="left:303px">Home</a>
  <a style="left:376px">Products</a>
  <a style="left:465px">Our Facilities</a>
  <a style="left:578px">Customers</a>
  <a style="left:678px">News</a>
  <a style="left:751px">Quotes</a>
  <a style="left:830px">Contact Us</a>
</nav>

<section>
  <div class="abs hero" role="img" aria-label="Photo of the PCB factory floor with production machines and conveyor rollers"></div>
  <div class="abs hero-shade"></div>
  <svg class="abs" style="left:0;top:600px" width="1200" height="170" viewBox="0 0 1200 170">
    <path d="M0 105 Q560 -10 1200 170 L0 170Z" fill="#e9e9e9"/>
    <path d="M0 108 Q520 20 1200 166 L1200 170 L0 170Z" fill="#fff"/>
  </svg>
  <h1 class="abs hero-title">Our Printed Circuit Board Business is Commited to "Excellence"</h1>
  <div class="abs hero-sub">Excellence in Quality, Prices, Services and On time Delivery</div>
  <div class="abs dots"><span class="on"></span><span></span><span></span><span></span></div>
  <div class="abs scroll-down"><svg width="16" height="18" viewBox="0 0 16 18" fill="none" stroke="#222" stroke-width="1.6"><path d="M8 1v15M2 10l6 6 6-6"/></svg></div>
</section>

<section>
  <h2 class="abs welcome-title">Welcome to Kolrith Global Limited (Kolrith)</h2>
  <div class="abs welcome-rule"></div>
  <div class="abs copy" style="left:90px;top:894px;width:444px">
    <p>Established in 2007, Kolrith Global Limited (Kolrith) is a Hong Kong company specializing in single and double sized printed circuit boards. Its manufacturing facility is located in a self-owned facility in Tangxia, Dongguan of China which is 50 minutes from Hong Kong.</p>
    <p>Our focus is to be a premium low costs PCB partner of our customers meeting their requirements in large quantity production as well as high mix low volume part numbers.</p>
  </div>
  <div class="abs copy" style="left:575px;top:894px;width:412px">
    <p>Through our insatiable drive to maximize efficiency, Kolrith is becoming a highly efficient PCB factory with an output to labor ratio of over 700 square meters per each worker and we aim at achieving 1,000 square meters by the end of 2018.</p>
    <p>PCB is our business and it is through continued automation and innovation that will drive our growth in the next 10 years.</p>
  </div>
  <div class="abs btn-products">View our products
    <svg width="15" height="12" viewBox="0 0 15 12" fill="none" stroke="#fff" stroke-width="1.6"><path d="M0 6h14M9 1l5 5-5 5"/></svg></div>
</section>

<section>
  <div class="abs contact-card"><h2>Contact us</h2></div>
  <div class="abs label" style="left:143px;top:1274px">Name:</div>
  <div class="abs label" style="left:451px;top:1274px">Email:</div>
  <div class="abs label" style="left:758px;top:1274px">Company name:</div>
  <div class="abs field" style="left:143px;top:1300px;width:301px;height:40px">Enter your name</div>
  <div class="abs field" style="left:451px;top:1300px;width:300px;height:40px">Enter your email address</div>
  <div class="abs field" style="left:758px;top:1300px;width:299px;height:40px">Enter your Company name</div>
  <div class="abs label" style="left:143px;top:1362px">Comments:</div>
  <div class="abs field" style="left:143px;top:1390px;width:914px;height:144px;align-items:flex-start;padding-top:14px">Enter your comments</div>
  <div class="abs submit">Submit</div>
</section>

<section>
  <div class="abs customers"><h2>Our Customers</h2></div>
  <div class="abs client" style="left:90px"><i></i>Norvane</div>
  <div class="abs client" style="left:268px">Brightwell Circuits</div>
  <div class="abs client" style="left:478px">Kestral</div>
  <div class="abs client" style="left:652px"><i></i>Lumora</div>
  <div class="abs client" style="left:807px">Tessaline</div>
  <div class="abs client" style="left:1012px"><i></i>Orvexa</div>
</section>

<section>
  <div class="abs cta"><h2>Need more information? Get in touch with us</h2></div>
  <div class="abs cta-btn">Contact us</div>
</section>

<footer>
  <div class="abs footer"></div>
  <div class="abs foot-brand">Kolrith</div>
  <div class="abs foot-h" style="left:343px">Quick Links</div>
  <ul class="abs foot-list" style="left:343px">
    <li>Home</li><li>Products</li><li>Our Facilities</li><li>Customers</li><li>News</li><li>Quotes</li><li>Contact Us</li>
  </ul>
  <div class="abs foot-h" style="left:573px">Contact information</div>
  <ul class="abs foot-list" style="left:573px">
    <li><svg width="11" height="11" viewBox="0 0 24 24"><path d="M6.6 10.8a15.1 15.1 0 0 0 6.6 6.6l2.2-2.2c.3-.3.7-.4 1-.2 1.1.4 2.3.6 3.6.6.6 0 1 .4 1 1V20c0 .6-.4 1-1 1A17 17 0 0 1 3 4c0-.6.4-1 1-1h3.5c.6 0 1 .4 1 1 0 1.3.2 2.5.6 3.6.1.3 0 .7-.2 1z"/></svg>Telephone: (852)29406158</li>
    <li><svg width="12" height="11" viewBox="0 0 24 22"><path d="M6 0h12v6H6zM0 8h24v10h-5v4H5v-4H0zM7 14v6h10v-6z"/></svg>Fax: (852)29406159</li>
    <li><svg width="12" height="10" viewBox="0 0 24 20"><path d="M0 2h24v2L12 11 0 4zM0 6l12 7 12-7v14H0z"/></svg>Email: Sales@kolrithpanel.com</li>
  </ul>
  <div class="abs foot-h" style="left:856px">Our Location</div>
  <ul class="abs foot-list" style="left:856px;line-height:22px;top:2260px">
    <li><svg width="10" height="13" viewBox="0 0 20 26"><path d="M10 0a10 10 0 0 1 10 10c0 7-10 16-10 16S0 17 0 10A10 10 0 0 1 10 0zm0 6a4 4 0 1 0 0 8 4 4 0 0 0 0-8z"/></svg>Kolrith Global Limited</li>
    <li style="padding-left:15px">28/F Harbour Crest</li>
    <li style="padding-left:15px">17 Marlow Road</li>
    <li style="padding-left:15px">Wan Chai, HONG KONG</li>
  </ul>
  <div class="abs foot-rule"></div>
  <div class="abs copyright">Copyright © 2018, Kolrith Global Limited. All Rights Reserved</div>
  <div class="abs to-top"><svg width="12" height="14" viewBox="0 0 12 14" fill="none" stroke="#222" stroke-width="1.5"><path d="M6 13V1M1 6l5-5 5 5"/></svg></div>
</footer>

</body>
</html>
```